依頼詳細
[ 歯科医院の特徴 ]
◆ ターゲット層
30代〜40代の女性がメインターゲット

派生してお子さんや年配の方までが通いやすい、
『家族で通えるような歯科医院』

◆ 推していく診療
オールマイティな診療(総合歯科診療)を行いつつ、
予防歯科・矯正歯科(Vuxa有り)・CAD/CAM(ミロナ)の患者を獲得。

◆ サイトで伝えていきたいこと
予防歯科の重要性
感染予防対策が行われている医院
早く、精密に行えるデジタルな診療

◆ 好きなサイトテイスト
https://www.wavelid-dentaloffice.example/

現代のサイトデザインの流行を取り入れ、
おしゃれではあるもののユーザーファーストなデザインを希望いたします。

また、Javascriptで多少のフェードインを想定しておりますので、
それに伴ったデザインを構成していただけますと幸いです。

内装パースデザイン, ロゴデザインを添付しております。
ご覧いただき、一貫性のあるサイトデザインをご提案いただけますと幸いです。

◆ 診療理念
患者様の笑顔と健康をサポートする
◇ 患者様によく説明し、納得、理解していただき歯科治療を行う
◇ 最新歯科治療、技術、サービスの日々研鑚取得
◇ 痛みの少ない治療の実施、低侵襲治療
◇ 行き届いた滅菌、衛生管理
◇ 自らの家族を呼べるような場所

◆ 医院の特徴
・可能な限り抜かない、削らない低侵襲治療(予防歯科の推奨)
・先進医療機器で治療の可能性を最大限に。
・安心して治療が受けられる衛生管理徹底
・矯正担当医によるソルテミーナ矯正・小児矯正
・患者様が通いやすい土日診療

◆ 診療時間
診療時間   月 火 水 木 金 土 日
09:30-13:00 ○ - ○ ○ ○ ○ ○
14:30-18:30 ○ - ○ ○ ○ ▲ ▲
▲:土日 (14:30-17:00)
休診日:火曜・祝日

◆ 院内紹介
①待合室
患者様に明るく広いリラックスできる空間を心がけています。

②キッズルーム
キッズルームやおむつ交換台もあるのでお子様連れのお母さんも安心です。

③完全バリアフリー設計
駐車場から治療室までバリアフリー設計になっています。ベビーカーでそのまま入れます。

④カウセリングルーム
お悩み事や診療への不安など気軽に相談ください。現在のお口の状態、治療計画、診療費用などをモニターを用いてご説明します。

⑤個室診療室
配慮したい時や、精密な治療などを行うときのために、個室診療室をご用意いたしました。静かな環境で、治療をお受けください。

⑥口腔外バキューム
歯の削りかすや血液などが空気中に飛び散るのを防ぐために口腔外バキュームを採用しております。口腔外バキュームは、口腔内バキュームの約2倍の吸収率で、粉塵を確実に吸い取ります。院内の衛生管理に、欠かせないアイテムです。
サイトURL
ページ数
1ページ
希望イメージ
シンプル 複雑
単色 カラフル
暗い 明るい
日常 高級
遊び心 厳粛
未来的 伝統的
女性的 男性的
希望する色
青系、水色系、茶系
納品ファイル
• 高解像度JPG (.jpg)
• イラストレーター形式 (.ai)
• PNG形式 (.png)
補足説明
TOPページだけでなく、SUBページもお願いできればと思い、
この度延長をいたしました。

◇ TOPページのデザイン(レスポンシブ)

◇ SUBページのテンプレートデザイン(レスポンシブ)
テンプレート化してそれを元に他ページを作成できるよう、
見出しタグや画像を使用した際のレイアウト例をお願いいたします。
[ 参考:https://www.tomorane-shika.example/sub.html ]

```html
<!DOCTYPE html>
<html lang="ja">
<head>
<meta charset="utf-8">
<title>HINATA デンタルクリニック</title>
<link rel="stylesheet" href="https://fonts.googleapis.com/css2?family=Noto+Serif+JP:wght@400;500;600&family=Noto+Sans+JP:wght@400;500&family=Cormorant+Garamond:wght@500;600&display=swap">
<style>
:root{
  --gold:#b49b6e;
  --gold-dark:#9c8257;
  --footer:#a98f62;
  --beige:#f8efe3;
  --beige-soft:#fbf6ef;
  --text:#5e5142;
  --text-light:#8a7c6a;
  --line:#e3d7c6;
  --white:#ffffff;
}
*{margin:0;padding:0;box-sizing:border-box}
html,body{width:1200px;height:4668px;overflow:hidden}
body{position:relative;background:var(--white);color:var(--text);font-family:"Noto Sans JP",sans-serif;font-size:13px;line-height:1.8}
.abs{position:absolute}
.serif{font-family:"Noto Serif JP",serif}
.en{font-family:"Cormorant Garamond",serif;letter-spacing:.12em;color:var(--gold);font-weight:600}
.btn{position:absolute;display:flex;align-items:center;justify-content:center;width:120px;height:32px;border-radius:16px;background:var(--gold);color:var(--white);font-family:"Cormorant Garamond",serif;font-size:13px;letter-spacing:.2em;font-weight:600}
.section-title{position:absolute;left:0;width:1200px;text-align:center}
.section-title .en{font-size:30px;display:block;line-height:1.2}
.section-title .ja{font-size:11px;color:var(--gold);letter-spacing:.1em}

/* header */
.site-header{left:0;top:0;width:1200px;height:48px;background:rgba(255,255,255,.95);display:flex;align-items:center;padding:0 10px 0 18px;z-index:5}
.brand{display:flex;align-items:center;gap:8px;color:var(--gold);font-family:"Noto Serif JP",serif;font-size:15px;font-weight:500;letter-spacing:.05em}
.brand-dot{width:22px;height:22px;border-radius:50%;background:var(--gold)}
.global-nav{display:flex;gap:26px;margin-left:auto;font-size:12px;color:var(--text)}
.header-tel{margin-left:34px;display:flex;align-items:center;gap:6px;font-family:"Cormorant Garamond",serif;font-size:19px;font-weight:600;color:var(--text)}
.header-reserve{margin-left:16px;width:92px;height:30px;border-radius:4px;background:var(--gold);color:#fff;font-size:12px;display:flex;align-items:center;justify-content:center}

/* hero */
.hero-visual{left:0;top:0;width:1200px;height:680px;background:linear-gradient(160deg,#f4eee6 0%,#e9ddcc 40%,#d8c3a4 70%,#efe6da 100%)}
.hero-copy{left:380px;top:264px;width:460px;height:58px;background:rgba(180,155,110,.88);color:#fff;font-family:"Noto Serif JP",serif;font-size:22px;white-space:nowrap;display:flex;align-items:center;justify-content:center;letter-spacing:.04em}

/* news */
.news{left:280px;top:608px;width:632px;height:220px;background:#fff;box-shadow:0 4px 18px rgba(120,100,70,.12);padding:20px 40px}
.news h2{font-size:22px;border-bottom:1px solid var(--line);padding-bottom:2px;width:90px;line-height:1.4}
.news ul{list-style:none;margin-top:8px}
.news li{font-size:11px;border-bottom:1px dotted var(--line);padding:4px 0;display:flex;gap:22px}
.news time{color:var(--gold)}
.news .btn{left:40px;top:176px;width:96px;height:26px}

/* policy */
.policy-photo{left:0;top:872px;width:512px;height:400px;background:linear-gradient(135deg,#cfe1ea,#e8d8cc 55%,#f3ebe3)}
.policy-panel{left:440px;top:928px;width:760px;height:412px;background:var(--beige)}
.policy-body{left:540px;top:960px;width:600px}
.policy-body .en{font-size:30px;line-height:1.1}
.policy-body .ja{font-size:11px;color:var(--gold)}
.policy-body h3{font-family:"Noto Serif JP",serif;font-size:26px;font-weight:500;color:var(--gold-dark);margin:6px 0 14px;letter-spacing:.04em}
.policy-list{list-style:none;width:440px}
.policy-list li{font-size:12px;border-bottom:1px solid var(--line);padding:5px 0;display:flex;gap:10px}
.policy-list span{font-family:"Cormorant Garamond",serif;font-size:16px;color:var(--gold);line-height:1.3}

/* feature */
.feature{left:0;top:1408px;width:1200px;height:632px;background:var(--beige)}
.feature-card{position:absolute;width:224px;height:228px;background:#fff}
.feature-card p{height:76px;display:flex;align-items:center;justify-content:center;text-align:center;font-size:12px;line-height:1.6;padding:0 10px}
.feature-card .ph{height:152px}
.feature-brand{left:760px;top:1832px;width:190px;text-align:center;color:var(--gold);font-family:"Noto Serif JP",serif;font-size:12px}
.feature-brand i{display:block;width:34px;height:34px;border-radius:50%;background:var(--gold);margin:0 auto 6px}

/* treatments */
.treatments{left:0;top:2072px;width:1200px;height:496px;background:linear-gradient(90deg,#f4f6f8 0%,#eef2f5 55%,#e2e8ee 100%)}
.treatment-item{position:absolute;width:96px;height:96px;border-radius:50%;background:var(--gold);color:#fff;font-size:11px;display:flex;flex-direction:column;align-items:center;justify-content:center;gap:6px;white-space:nowrap}
.treatment-item i{width:22px;height:22px;border:2px solid rgba(255,255,255,.85);border-radius:50%}

/* equipments */
.equip{position:absolute;width:240px}
.equip .ph{height:140px}
.equip h4{font-size:11px;color:var(--gold);font-weight:500;margin-top:10px}
.equip p{font-size:10px;line-height:1.6;color:var(--text-light)}

/* greeting */
.greeting-panel{left:0;top:3380px;width:740px;height:412px;background:var(--beige)}
.greeting-photo{left:720px;top:3340px;width:252px;height:360px;background:linear-gradient(160deg,#eef3f6,#cfdde6 60%,#b9c9d4)}
.greeting-body{left:224px;top:3420px;width:460px}
.greeting-body .en{font-size:30px;line-height:1.1}
.greeting-body .ja{font-size:11px;color:var(--gold)}
.greeting-body p{font-size:11px;line-height:2;margin-top:10px}
.greeting-body .sign{text-align:right;margin-top:8px}

/* map */
.access-map{left:0;top:3860px;width:1200px;height:348px;background:linear-gradient(135deg,#e9eaea,#dcdfdf 50%,#e6e4e0)}

/* footer */
.site-footer{left:0;top:4208px;width:1200px;height:460px;background:var(--footer);color:#fff}
.footer-brand{position:absolute;left:0;top:40px;width:1200px;display:flex;justify-content:center;align-items:center;gap:10px;font-family:"Noto Serif JP",serif;font-size:20px}
.footer-brand i{width:28px;height:28px;border-radius:50%;background:#fff}
.footer-building{position:absolute;left:332px;top:104px;width:288px;height:248px;background:linear-gradient(180deg,#dfe6ea,#c9ced0 60%,#b7b0a4)}
.footer-nav{position:absolute;top:108px;font-size:11px;line-height:1.9;list-style:none}
.hours{position:absolute;left:660px;top:220px;width:420px;border-collapse:collapse;font-size:11px}
.hours th,.hours td{border-bottom:1px solid rgba(255,255,255,.45);padding:3px 0;text-align:center;font-weight:400;height:26px}
.hours th:first-child,.hours td:first-child{text-align:left;width:110px}
.open-mark{display:inline-block;width:10px;height:10px;border:1.5px solid #fff;border-radius:50%;vertical-align:middle}
.tri-mark{display:inline-block;vertical-align:middle}
.hours-note{position:absolute;left:660px;top:312px;font-size:10px}
.footer-tel{position:absolute;left:660px;top:340px;font-family:"Cormorant Garamond",serif;font-size:30px;font-weight:600;letter-spacing:.04em}
.copyright{position:absolute;left:0;top:420px;width:1200px;text-align:center;font-size:10px;opacity:.85}
</style>
</head>
<body>

<div class="hero-visual abs" role="img" aria-label="明るい木目調の受付カウンターがある医院エントランスの写真"></div>

<header class="site-header abs">
  <div class="brand"><span class="brand-dot"></span>HINATA デンタルクリニック</div>
  <nav class="global-nav"><span>診療案内</span><span>初めての方へ</span><span>ドクター紹介</span><span>医院案内</span><span>料金表</span><span>アクセス</span></nav>
  <div class="header-tel">
    <svg width="14" height="14" viewBox="0 0 24 24"><path fill="#b49b6e" d="M6.6 10.8a15 15 0 0 0 6.6 6.6l2.2-2.2c.3-.3.7-.4 1-.2 1.1.4 2.3.6 3.6.6.6 0 1 .4 1 1V20c0 .6-.4 1-1 1A17 17 0 0 1 3 4c0-.6.4-1 1-1h3.5c.6 0 1 .4 1 1 0 1.3.2 2.5.6 3.6.1.3 0 .7-.2 1z"/></svg>
    1,000-000-0000
  </div>
  <div class="header-reserve">WEB予約</div>
</header>

<div class="hero-copy abs">患者様の笑顔と健康をサポートします。</div>

<section class="news abs">
  <h2 class="en">NEWS</h2>
  <ul>
    <li><time>2020.00.00</time>年末年始の休診日についてのお知らせを掲載しました。</li>
    <li><time>2020.00.00</time>感染予防対策の取り組みについてご案内いたします。</li>
    <li><time>2020.00.00</time>土日診療の受付時間が一部変更となりました。</li>
  </ul>
  <span class="btn">MORE</span>
</section>

<div class="policy-photo abs" role="img" aria-label="診察台で笑顔を見せる女性患者の写真"></div>
<div class="policy-panel abs"></div>
<section class="policy-body abs">
  <span class="en">POLICY</span><br><span class="ja">診療理念</span>
  <h3>患者様の笑顔と健康をサポートします。</h3>
  <ol class="policy-list">
    <li><span>1</span>患者様によく説明し、納得、理解していただき歯科治療を行う</li>
    <li><span>2</span>最新歯科治療、技術、サービスの日々研鑚取得</li>
    <li><span>3</span>痛みの少ない治療の実施、低侵襲治療</li>
    <li><span>4</span>行き届いた滅菌、衛生管理</li>
    <li><span>5</span>自らの家族を呼べるような場所</li>
  </ol>
</section>
<span class="btn" style="left:700px;top:1284px">MORE</span>

<section class="feature abs"></section>
<div class="section-title" style="top:1450px"><span class="en">FEATURE</span><span class="ja">当院の特徴</span></div>
<div class="feature-card" style="left:248px;top:1540px"><p>可能な限り抜かない、削らない<br>低侵襲治療（予防歯科の推奨）</p><div class="ph" role="img" aria-label="歯を見せて微笑む女性の写真" style="background:linear-gradient(135deg,#f1e3d6,#e2cbb8)"></div></div>
<div class="feature-card" style="left:488px;top:1540px"><p>先進医療機器で<br>治療の可能性を最大限に。</p><div class="ph" role="img" aria-label="先進的な歯科医療機器の写真" style="background:linear-gradient(135deg,#e6eaee,#c9d1d8)"></div></div>
<div class="feature-card" style="left:728px;top:1540px"><p>安心して治療が受けられる<br>衛生管理徹底</p><div class="ph" role="img" aria-label="滅菌器の写真" style="background:linear-gradient(135deg,#dfe3e6,#b6bec4)"></div></div>
<div class="feature-card" style="left:248px;top:1792px"><p>矯正担当医による<br>ソルテミーナ矯正・小児矯正</p><div class="ph" role="img" aria-label="透明なマウスピース矯正装置の写真" style="background:linear-gradient(135deg,#eef1f3,#d5dde2)"></div></div>
<div class="feature-card" style="left:488px;top:1792px"><p>患者様が通いやすい<br>土日診療</p><div class="ph" role="img" aria-label="待合で過ごす家族の写真" style="background:linear-gradient(135deg,#efe4d6,#d9c4ab)"></div></div>
<div class="feature-brand abs"><i></i>HINATA DENTAL CLINIC</div>
<span class="btn" style="left:795px;top:1920px">MORE</span>

<section class="treatments abs" role="img" aria-label="淡い色調の歯科器具の写真を背景にした診療案内エリア"></section>
<div class="section-title" style="top:2118px"><span class="en">TREATMENTS</span><span class="ja">診療案内</span></div>
<div class="treatment-item" style="left:312px;top:2220px"><i></i>一般歯科</div>
<div class="treatment-item" style="left:432px;top:2220px"><i></i>予防歯科</div>
<div class="treatment-item" style="left:552px;top:2220px"><i></i>小児歯科</div>
<div class="treatment-item" style="left:672px;top:2220px"><i></i>矯正歯科</div>
<div class="treatment-item" style="left:792px;top:2220px"><i></i>審美歯科</div>
<div class="treatment-item" style="left:312px;top:2340px"><i></i>口腔外科</div>
<div class="treatment-item" style="left:432px;top:2340px"><i></i>インプラント</div>
<div class="treatment-item" style="left:552px;top:2340px"><i></i>入れ歯</div>
<div class="treatment-item" style="left:672px;top:2340px"><i></i>ホワイトニング</div>
<div class="treatment-item" style="left:792px;top:2340px"><i></i>小児矯正</div>

<div class="section-title" style="top:2618px"><span class="en">EQUIPMENTS</span><span class="ja">院内紹介</span></div>
<div class="equip" style="left:228px;top:2708px"><div class="ph" role="img" aria-label="明るく広い待合室の写真" style="background:linear-gradient(135deg,#f3ede4,#e0d2bd)"></div><h4>待合室</h4><p>患者様に明るく広いリラックスできる空間を心がけています。</p></div>
<div class="equip" style="left:484px;top:2708px"><div class="ph" role="img" aria-label="カラフルな遊具があるキッズルームの写真" style="background:linear-gradient(135deg,#f3e6c8,#cfe0e8)"></div><h4>キッズルーム</h4><p>キッズルームやおむつ交換台もあるのでお子様連れのお母さんも安心です。</p></div>
<div class="equip" style="left:740px;top:2708px"><div class="ph" role="img" aria-label="ベビーカーの写真" style="background:linear-gradient(135deg,#f1f1f0,#c9c6c2)"></div><h4>完全バリアフリー設計</h4><p>駐車場から治療室までバリアフリー設計になっています。ベビーカーでそのまま入れます。</p></div>
<div class="equip" style="left:228px;top:2952px"><div class="ph" role="img" aria-label="モニターのあるカウンセリングルームの写真" style="background:linear-gradient(135deg,#f0ebe4,#d8ccbb)"></div><h4>カウンセリングルーム</h4><p>お悩み事や診療への不安など気軽に相談ください。治療計画や費用をモニターでご説明します。</p></div>
<div class="equip" style="left:484px;top:2952px"><div class="ph" role="img" aria-label="個室診療室の写真" style="background:linear-gradient(135deg,#dfe8ee,#9fb6c6)"></div><h4>個室診療室</h4><p>配慮したい時や精密な治療のために個室診療室をご用意。静かな環境で治療をお受けください。</p></div>
<div class="equip" style="left:740px;top:2952px"><div class="ph" role="img" aria-label="口腔外バキュームを使った治療の写真" style="background:linear-gradient(135deg,#cfd8e0,#5f6f7e)"></div><h4>口腔外バキューム</h4><p>歯の削りかすや血液などが空気中に飛び散るのを防ぎ、粉塵を確実に吸い取ります。</p></div>
<span class="btn" style="left:540px;top:3246px">MORE</span>

<div class="greeting-panel abs"></div>
<div class="greeting-photo abs" role="img" aria-label="白衣を着た院長の写真"></div>
<section class="greeting-body abs">
  <span class="en">GREETING</span><br><span class="ja">院長挨拶</span>
  <p>当院のホームページをご覧いただき、誠にありがとうございます。</p>
  <p>地域の皆様が家族で安心して通える歯科医院を目指しています。</p>
  <p>予防を大切にし、できる限り抜かない、削らない治療を心がけております。丁寧な説明と納得いただける治療計画をご提案し、最新の設備と徹底した衛生管理のもとで診療を行います。お口のことで気になることがございましたら、どうぞお気軽にご相談ください。</p>
  <p class="sign">HINATA デンタルクリニック 院長　山田 太郎</p>
</section>
<span class="btn" style="left:344px;top:3720px">MORE</span>

<div class="access-map abs" role="img" aria-label="医院周辺の地図"></div>

<footer class="site-footer abs">
  <div class="footer-brand"><i></i>HINATA デンタルクリニック</div>
  <div class="footer-building" role="img" aria-label="医院の外観写真"></div>
  <ul class="footer-nav" style="left:660px"><li>・ホーム</li><li>・初めての方へ</li><li>・医院案内</li></ul>
  <ul class="footer-nav" style="left:780px"><li>・診療案内</li><li>・一般歯科</li><li>・予防歯科</li><li>・矯正歯科</li></ul>
  <ul class="footer-nav" style="left:920px"><li>・料金表</li><li>・アクセス</li><li>・WEB予約</li></ul>
  <table class="hours">
    <tr><th>診療時間</th><th>月</th><th>火</th><th>水</th><th>木</th><th>金</th><th>土</th><th>日</th></tr>
    <tr><td>09:30-13:00</td><td><span class="open-mark"></span></td><td>-</td><td><span class="open-mark"></span></td><td><span class="open-mark"></span></td><td><span class="open-mark"></span></td><td><span class="open-mark"></span></td><td><span class="open-mark"></span></td></tr>
    <tr><td>14:30-18:30</td><td><span class="open-mark"></span></td><td>-</td><td><span class="open-mark"></span></td><td><span class="open-mark"></span></td><td><span class="open-mark"></span></td><td><svg class="tri-mark" width="11" height="10" viewBox="0 0 11 10"><path d="M5.5 0L11 10H0z" fill="#fff"/></svg></td><td><svg class="tri-mark" width="11" height="10" viewBox="0 0 11 10"><path d="M5.5 0L11 10H0z" fill="#fff"/></svg></td></tr>
  </table>
  <p class="hours-note"><svg class="tri-mark" width="9" height="8" viewBox="0 0 11 10"><path d="M5.5 0L11 10H0z" fill="#fff"/></svg>:土日 (14:30-17:00)　休診日:火曜・祝日</p>
  <p class="footer-tel">tel.000-000-0000</p>
  <p class="copyright">© HINATA DENTAL CLINIC All Rights Reserved.</p>
</footer>

</body>
</html>
```